Office Wall Poster plus other Wall Decal quotes in office

We have redesigned our office & require parts of our Culture statement to be displayed in our office. Our company is VOLO Estate Agents Group and our brand is all about being VOLO .. integrity, honesty, authenticity etc.
We have two areas we wish to decorate.
1. Reception
2. Meeting Room

RECEPTION
We want our leading culture statement to be displayed as large A0 size in a framed POSTER PRINT in our reception. The frame will be black.
WORDING: 'There's a reason we're called VOLO. VOLO is the essence of who we are'
Our brand colors are red, white, black. Our Red is CMYK 12,99, 92,02
When we type our name VOLO, we always use Venera font (always in caps). I have attached a file I personally created with 3 different ideas (I am not a designer) but we are not happy with any of them but it will give you an idea of what we are looking for. We want a simple statement so it stands out and not too busy.

MEETING ROOM
We have one black feature wall in this room and wish to dress this with a collection of quotes from our main Culture statement. We will have these printed as 'stick on wall decals' We have provided a collection of 8 quotes for you to design. Wording is to be in white colour with the key words to be METALLIC SILVER & in caps. We were planning to arrange them ad-hoc on the wall singularly, but if you have any creative ideas on how to display these, we are open to suggestions. Please provide your ideas on how best to arrange these on the black wall. Maybe even in a circle to represent our logo? But we truly do not have a clue - we are only real estate agents, not designers. That is why we would love suggetions on how best to make our Culture Statements work best.
Best of luck and we are excited to see your ideas!

Our clients need to get a great feel for what we are all about when they visit our office. Our culture needs to be seen and felt.

Real Estate

• We use Venera font when we type our name VOLO

EB3D1F
EC4F4E
F09395
F8D3D4
FCEDEE

• Not too busy, simple statements, easy to read

```html
<!DOCTYPE html>
<html lang="en">
<head>
<meta charset="utf-8">
<title>VOLO Estate Agents Group – Reception Poster</title>
<link rel="stylesheet" href="https://fonts.googleapis.com/css2?family=Inter:wght@300;700&family=Noto+Serif:wght@400&display=swap">
<style>
  :root {
    --wall: #e6e6e6;
    --poster-black: #171717;
    --brand-red: #b94447;
    --disc-red: #c23a33;
    --paper-white: #eeeeee;
    --caption-grey: #d9d9d9;
  }
  * { margin: 0; padding: 0; box-sizing: border-box; }
  html, body {
    width: 1200px;
    height: 796px;
    overflow: hidden;
    background: var(--wall);
  }
  .poster {
    position: absolute;
    left: 330px;
    top: 18px;
    width: 539px;
    height: 760px;
    background: var(--poster-black);
  }
  .headline {
    position: absolute;
    left: 50px;
    top: 56px;
    font-family: "Inter", Arial, sans-serif;
    font-weight: 700;
    font-size: 82px;
    line-height: 68px;
    letter-spacing: -2.5px;
    color: var(--brand-red);
  }
  .headline span { display: block; }
  .brand-word {
    position: absolute;
    left: 47px;
    top: 328px;
    font-family: "Noto Serif", Georgia, serif;
    font-weight: 400;
    font-size: 140px;
    line-height: 1;
    color: var(--paper-white);
    letter-spacing: 1px;
  }
  .tagline {
    position: absolute;
    right: 117px;
    top: 678px;
    font-family: "Inter", Arial, sans-serif;
    font-weight: 300;
    font-size: 12.5px;
    color: var(--caption-grey);
    white-space: nowrap;
  }
  .tagline .tagline-name {
    font-family: "Noto Serif", Georgia, serif;
    font-weight: 400;
    font-size: 13.5px;
  }
  .brand-disc {
    position: absolute;
    left: 427px;
    top: 646px;
    width: 82px;
    height: 82px;
    border-radius: 50%;
    background: var(--disc-red);
  }
  .brand-name {
    position: absolute;
    right: 30px;
    top: 735px;
    font-family: "Inter", Arial, sans-serif;
    font-weight: 300;
    font-size: 9px;
    letter-spacing: 0.3px;
    color: var(--caption-grey);
    white-space: nowrap;
  }
</style>
</head>
<body>
  <main class="poster">
    <h1 class="headline">
      <span>There's</span>
      <span>a reason</span>
      <span>we're</span>
      <span>called</span>
    </h1>
    <p class="brand-word">VOLO</p>
    <p class="tagline"><span class="tagline-name">VOLO</span> is the essence of who we are.</p>
    <div class="brand-disc" aria-hidden="true"></div>
    <p class="brand-name">VOLO Estate Agents Group</p>
  </main>
</body>
</html>
```